E-commerce homepage webdesign

Hello,

I would like to get a new homepage for my E-commerce website.

I will send you my logo and you can use product pictures from my website or Glimmerbank to create the mockup.

I created a brief in the document joined.

```html
<!DOCTYPE html>
<html lang="fr">
<head>
<meta charset="utf-8">
<title>Stampoli – Objets publicitaires</title>
<link href="https://fonts.googleapis.com/css2?family=Hind:wght@400;500;600&family=Poppins:wght@300;400;500;600&display=swap" rel="stylesheet">
<style>
:root{
  --navy:#0e2452;
  --navy-deep:#0a1c44;
  --indigo:#221c6a;
  --lavender:#8c86bb;
  --orange:#f26522;
  --price:#e8552a;
  --star:#f5a623;
  --grey-bg:#efefef;
  --text:#2b2b2b;
  --footer:#3b3b3d;
  --line:#e2e2e2;
}
*{box-sizing:border-box;margin:0;padding:0}
html,body{width:1200px;height:4761px;overflow:hidden}
body{position:relative;background:#fff;font-family:"Poppins",sans-serif;color:var(--text)}
.abs{position:absolute}

/* top strip */
.top-strip{left:0;top:0;width:1200px;height:37px;background:var(--navy);color:#fff;font-size:11.5px;font-weight:500}
.top-strip span{position:absolute;top:11px;display:flex;align-items:center;gap:10px}
.top-strip svg{width:16px;height:16px;fill:#fff}

/* brand name */
.brand{display:flex;align-items:center;gap:12px}
.brand-square{width:30px;height:30px;background:var(--orange)}
.brand-name{font-family:"Poppins",sans-serif;font-weight:400;font-size:26px;line-height:1;color:#333}

/* header */
.search{left:388px;top:78px;width:328px;height:37px;border:1px solid #ddd;font-size:10px;color:#999;padding:12px 18px}
.search svg{position:absolute;right:12px;top:10px;width:16px;height:16px}
.phone{left:776px;top:80px;font-size:14px;color:var(--orange)}
.phone small{display:block;color:#333;font-size:9.5px;text-align:right;margin-top:1px}
.avatar{left:919px;top:70px;width:40px;height:48px;border-radius:50%;background:radial-gradient(circle at 50% 40%,#e9d6c8,#b9a79b)}
.cart{left:998px;top:82px}
.cart-count{left:1018px;top:74px;font-size:9px;color:var(--navy)}
.lang{left:1045px;top:83px;width:39px;height:22px;border:1.5px solid var(--navy);font-size:11px;text-align:center;line-height:19px;font-weight:500}
.shop-bar{left:0;top:142px;width:1200px;height:21px;background:var(--navy-deep);color:#fff;font-size:10px;font-weight:600;padding:4px 0 0 117px}

/* hero grid */
.tile{width:311px;height:313px}
.tile-label{color:#fff;font-family:"Hind",sans-serif;font-size:28px;display:flex;align-items:center;justify-content:center;letter-spacing:.5px}
.category-menu{left:105px;top:172px;width:172px;height:277px;background:#fff;box-shadow:0 2px 8px rgba(0,0,0,.18);padding:10px 0 0 14px}
.category-menu li{list-style:none;height:23px;font-size:8.5px;color:#555;display:flex;align-items:center;gap:8px;position:relative;letter-spacing:.3px}
.category-menu li.active{color:var(--orange)}
.category-menu li i{width:10px;height:10px;border:1px solid currentColor;border-radius:2px;display:inline-block}
.category-menu li b{position:absolute;right:10px;font-weight:400;color:#999}

/* section titles */
.section-title{display:flex;gap:14px}
.section-title .bar{width:4px;background:var(--orange)}
.section-title h2{font-family:"Hind",sans-serif;font-weight:400;font-size:29px;line-height:1.1}
.section-title p{font-family:"Hind",sans-serif;font-size:20px;margin-top:4px}

/* advantages */
.advantages{left:0;top:937px;width:1200px;height:363px;background:var(--grey-bg)}
.adv-card{top:111px;width:311px;height:185px;background:#fff;text-align:center;padding:22px 22px 0}
.adv-card h3{font-size:14px;font-weight:500;line-height:1.25;color:#222;height:38px}
.adv-card p{font-size:10px;color:#aaa;line-height:1.85;margin-top:14px}

/* banner */
.banner{left:0;top:1300px;width:1200px;height:490px;background:radial-gradient(circle at 85% 45%,#6b2a24 0%,#3a2420 25%,#261c1a 60%,#1d1716 100%)}
.banner h2{position:absolute;left:115px;top:150px;font-family:"Hind",sans-serif;font-weight:400;font-size:48px;color:#fff}
.banner p{position:absolute;left:115px;top:232px;font-family:"Hind",sans-serif;font-size:30px;color:#fff}
.banner a{position:absolute;left:115px;top:327px;width:120px;height:43px;border:1px solid #fff;color:#fff;font-size:12px;text-align:center;line-height:41px;text-decoration:none}

/* products */
.product{top:2040px;width:311px;height:534px;border:1px solid var(--line);text-align:center}
.product .photo{position:absolute;left:55px;top:30px;width:200px;height:250px;background:linear-gradient(180deg,#f4f4f4,#2a2a2a 50%,#f4f4f4)}
.product h3{position:absolute;left:0;right:0;top:313px;font-family:"Hind",sans-serif;font-weight:400;font-size:23px;color:#222}
.product .price{position:absolute;left:0;right:0;top:356px;font-family:"Hind",sans-serif;font-size:28px;color:var(--price)}
.stars{color:var(--star);letter-spacing:5px}
.product .stars{position:absolute;left:0;right:0;top:401px;font-size:20px}
.product .actions{position:absolute;left:48px;right:48px;top:461px;display:flex;justify-content:space-between;align-items:center;font-size:15px;color:#444}
.product .actions span{display:flex;align-items:center;gap:10px}

/* testimonials */
.review{top:3051px;width:475px;height:214px;background:#fff;padding:20px 38px 0}
.review .who{display:flex;gap:14px;align-items:flex-start}
.review .pic{width:42px;height:42px;border-radius:50%;background:radial-gradient(circle,#e4c9ae,#a88d76)}
.review h4{font-family:"Hind",sans-serif;font-weight:400;font-size:19px;line-height:1.1}
.review small{display:block;font-size:10px;margin-top:5px}
.review .stars{font-size:14px;letter-spacing:3px}
.review p{font-size:10.5px;line-height:1.85;color:#555;margin-top:14px;padding-left:18px;text-indent:-18px}
.review p q{quotes:none;color:#333;font-weight:600;margin-right:6px}
.review .tail{position:absolute;left:80px;bottom:-25px;width:0;height:0;border-right:38px solid transparent;border-top:26px solid #fff}
.dots{left:550px;top:3351px;display:flex;gap:20px}
.dots i{width:42px;height:4px;background:#fff}

/* catalogue */
.catalogue{left:0;top:3448px;width:1200px;height:440px;background:var(--grey-bg)}
.catalogue .intro{position:absolute;left:195px;width:810px;top:185px;text-align:center;font-size:19px;line-height:1.6;color:#6d6d6d}
.catalogue a{position:absolute;left:496px;top:315px;width:209px;height:59px;background:var(--orange);border-radius:10px 10px 0 10px;color:#fff;font-size:15px;text-align:center;line-height:59px;text-decoration:none;font-weight:500}

/* accordion */
.accordion{left:115px;top:3981px;width:970px;border:1px solid var(--navy)}
.acc-head{height:35px;background:var(--navy-deep);color:#fff;font-size:14.5px;padding:0 16px;display:flex;align-items:center;justify-content:space-between;border-bottom:1px solid #fff}
.acc-head .sign{font-size:22px;font-weight:300}
.acc-body{height:158px;padding:10px 16px;font-size:10.5px;line-height:1.85;color:#888;background:#fff}

/* footer */
.footer{left:0;top:4456px;width:1200px;height:305px;background:var(--footer);color:#fff}
.footer h5{font-size:12px;font-weight:500;margin-bottom:18px}
.footer ul{list-style:none;font-size:10.5px;line-height:1.85;color:#ddd}
.footer .about{font-size:10px;line-height:1.9;color:#ddd}
.social li{display:flex;align-items:center;gap:10px;margin-bottom:14px}
.social li i{width:12px;height:12px;border-radius:50%;background:#fff}
.newsletter{display:flex;margin-top:18px}
.newsletter span{width:148px;height:30px;background:#fff;color:#888;font-size:10px;padding:9px 10px}
.newsletter b{width:64px;height:30px;background:var(--orange);font-size:10px;font-weight:500;text-align:center;line-height:30px}
.pay{display:flex;gap:10px;position:absolute;left:115px;top:257px}
.pay span{width:48px;height:28px;background:#fff;color:#333;font-size:9px;font-weight:500;display:flex;align-items:center;justify-content:center}
</style>
</head>
<body>

<div class="abs top-strip">
  <span style="left:116px"><svg viewBox="0 0 24 24"><path d="M1 5h14v10H1zM15 9h4l3 3v3h-7z"/><circle cx="6" cy="17" r="2"/><circle cx="18" cy="17" r="2"/></svg>Quick delivery</span>
  <span style="left:357px"><svg viewBox="0 0 24 24"><path d="M3 21l4-1L20 7l-3-3L4 17zM16 3l3 3 2-2-3-3z"/></svg>Free digital printing proof</span>
  <span style="left:650px"><svg viewBox="0 0 24 24"><path d="M12 2a10 10 0 100 20 10 10 0 000-20zm-1.5 14.5L6 12l1.4-1.4 3.1 3.1 6.1-6.1L18 9z"/></svg>Personalised followed-up</span>
  <span style="left:945px"><svg viewBox="0 0 24 24"><path d="M12 2a10 10 0 100 20 10 10 0 000-20zM8 9a1.3 1.3 0 110 2.6A1.3 1.3 0 018 9zm8 0a1.3 1.3 0 110 2.6A1.3 1.3 0 0116 9zm-4 9c-2.8 0-5-2-5.5-4h11c-.5 2-2.7 4-5.5 4z"/></svg>98% satisfied clients</span>
</div>

<div class="abs brand" style="left:115px;top:82px">
  <div class="brand-square"></div>
  <div class="brand-name">Stampoli</div>
</div>
<div class="abs search">Chercher produit ou marque
  <svg viewBox="0 0 24 24" fill="none" stroke="#222" stroke-width="3"><circle cx="10" cy="10" r="7"/><path d="M15 15l6 6"/></svg>
</div>
<div class="abs phone">&#9990; +32 10 48 22 60<small>Appelez Léa</small></div>
<div class="abs avatar" role="img" aria-label="Photo de la conseillère clientèle"></div>
<svg class="abs cart" width="24" height="22" viewBox="0 0 24 22"><path d="M0 1h4l3 12h13l3-9H6" fill="none" stroke="#0e2452" stroke-width="2.4"/><path d="M7 5h15l-2.5 7H8.5z" fill="#0e2452"/><circle cx="9" cy="18" r="2.2" fill="#0e2452"/><circle cx="19" cy="18" r="2.2" fill="#0e2452"/></svg>
<div class="abs cart-count">2</div>
<div class="abs lang">EN</div>
<div class="abs shop-bar">SHOP BY CATEGORY</div>

<div class="abs tile" style="left:115px;top:205px;background:linear-gradient(135deg,#d9d3c7,#e4792f 55%,#b3683a)" role="img" aria-label="Sac à dos orange personnalisé"></div>
<div class="abs tile tile-label" style="left:444px;top:205px;background:linear-gradient(160deg,#3d5a8e,#2a4677)" role="img" aria-label="Gourde en verre sur fond bleu">WATER BOTTLE</div>
<div class="abs tile" style="left:773px;top:205px;background:linear-gradient(160deg,#bca88a,#efeeea 50%,#8e6f52)" role="img" aria-label="Pile de t-shirts blancs sur un tabouret"></div>
<div class="abs tile" style="left:115px;top:536px;background:linear-gradient(135deg,#a4d4ea,#8ec7e1 50%,#7d8d96)" role="img" aria-label="Gourde de sport grise avec logo personnalisé"></div>
<div class="abs tile" style="left:444px;top:536px;background:linear-gradient(160deg,#e8e6e2,#2d2d2f 55%,#d8d2c8)" role="img" aria-label="Pochette et maniques noires en coton"></div>
<div class="abs tile" style="left:773px;top:536px;background:linear-gradient(160deg,#e9e7e4,#3a3a3c 55%,#c9c6c2)" role="img" aria-label="Parapluie pliant noir"></div>

<ul class="abs category-menu">
  <li class="active"><i></i>CLOTHES<b>›</b></li>
  <li><i></i>ELECTRONICS<b>›</b></li>
  <li><i></i>SPORT &amp; HOBBIES</li>
  <li><i></i>INTERIOR DESIGN</li>
  <li><i></i>ACCESSORIES<b>›</b></li>
  <li><i></i>TOYS</li>
  <li><i></i>FOODS &amp; DRINKS</li>
  <li><i></i>JEWELS</li>
  <li><i></i>HOLIDAYS &amp; GIFT IDEAS</li>
  <li><i></i>CAR &amp; MOTO SALES</li>
</ul>

<section class="abs advantages">
  <div class="abs section-title" style="left:493px;top:36px"><div class="bar" style="height:50px"></div><h2 style="padding-top:10px">Nos avantages</h2></div>
  <div class="abs adv-card" style="left:115px"><h3>Aperçu numérique gratuit avant commande</h3><p>Pour toute demande ou commande, vous recevez un aperçu numérique gratuit à valider ainsi que l'offre de prix sans engagement en moins de 24h.</p></div>
  <div class="abs adv-card" style="left:444px"><h3>Frais de modification graphique offerts</h3><p>Votre logo n'est pas au bon format ou a besoin d'être modifié avant impression ? Pas de problème, notre équipe de graphistes s'en occupe sans frais supplémentaires.</p></div>
  <div class="abs adv-card" style="left:773px"><h3>Plus de 30.000 produits disponibles</h3><p>Choisissez vos objets publicitaires dans notre large gamme. Vous ne trouvez pas votre bonheur ? Contactez-nous ! Notre équipe cherchera pour vous le produit idéal.</p></div>
</section>

<section class="abs banner" role="img" aria-label="Boule de Noël rouge suspendue à une branche de sapin">
  <h2>The arrival of a new product</h2>
  <p>Christmas products</p>
  <a>VIEW MORE</a>
</section>

<div class="abs section-title" style="left:491px;top:1891px"><div class="bar" style="height:62px"></div><div><h2>Nos références</h2><p>Découvrez nos dernières créations</p></div></div>

<div class="abs product" style="left:115px">
  <div class="photo" role="img" aria-label="Montre LED noire"></div>
  <h3>Lorem ipsum dolor</h3><div class="price">$89</div><div class="stars">★★★★★</div>
  <div class="actions"><span><svg width="24" height="20" viewBox="0 0 24 22"><path d="M0 1h4l3 12h13l3-9H6" fill="none" stroke="#444" stroke-width="2"/><circle cx="9" cy="18" r="2" fill="#444"/><circle cx="19" cy="18" r="2" fill="#444"/></svg>ADD TO CART</span><svg width="22" height="20" viewBox="0 0 24 22"><path d="M12 20S2 13 2 7a5 5 0 0110-1 5 5 0 0110 1c0 6-10 13-10 13z" fill="none" stroke="#444" stroke-width="2"/></svg></div>
</div>
<div class="abs product" style="left:444px">
  <div class="photo" role="img" aria-label="Chargeur allume-cigare noir"></div>
  <h3>Lorem ipsum dolor</h3><div class="price">$89</div><div class="stars">★★★★★</div>
  <div class="actions"><span><svg width="24" height="20" viewBox="0 0 24 22"><path d="M0 1h4l3 12h13l3-9H6" fill="none" stroke="#444" stroke-width="2"/><circle cx="9" cy="18" r="2" fill="#444"/><circle cx="19" cy="18" r="2" fill="#444"/></svg>ADD TO CART</span><svg width="22" height="20" viewBox="0 0 24 22"><path d="M12 20S2 13 2 7a5 5 0 0110-1 5 5 0 0110 1c0 6-10 13-10 13z" fill="none" stroke="#444" stroke-width="2"/></svg></div>
</div>
<div class="abs product" style="left:773px">
  <div class="photo" role="img" aria-label="Batterie externe noire personnalisée"></div>
  <h3>Lorem ipsum dolor</h3><div class="price">$89</div><div class="stars">★★★★★</div>
  <div class="actions"><span><svg width="24" height="20" viewBox="0 0 24 22"><path d="M0 1h4l3 12h13l3-9H6" fill="none" stroke="#444" stroke-width="2"/><circle cx="9" cy="18" r="2" fill="#444"/><circle cx="19" cy="18" r="2" fill="#444"/></svg>ADD TO CART</span><svg width="22" height="20" viewBox="0 0 24 22"><path d="M12 20S2 13 2 7a5 5 0 0110-1 5 5 0 0110 1c0 6-10 13-10 13z" fill="none" stroke="#444" stroke-width="2"/></svg></div>
</div>

<svg class="abs" style="left:0;top:2680px" width="1200" height="770" viewBox="0 0 1200 770">
  <path d="M0 115 C250 30 450 150 750 60 S1100 -8 1200 18 L1200 770 L0 770Z" fill="#8c86bb"/>
  <path d="M0 140 C250 55 450 170 760 80 S1100 22 1200 40 L1200 770 L0 770Z" fill="#221c6a"/>
</svg>
<div class="abs section-title" style="left:489px;top:2934px"><div class="bar" style="height:52px"></div><h2 style="color:#fff;padding-top:12px">Qu'en pensent nos clients ?</h2></div>

<div class="abs review" style="left:115px">
  <div class="who"><div class="pic" role="img" aria-label="Photo de la cliente"></div><div><h4>Marine D. (Liège)</h4><small>CO-Founder</small><div class="stars">★★★★★</div></div></div>
  <p><q>“</q>Nous avons commandé 200 gourdes en inox pour les élèves de notre école dans le cadre de notre opération « Zéro déchet ». Elles sont parfaites ! Très belle impression et gourdes d'excellente qualité.</p>
  <div class="tail"></div>
</div>
<div class="abs review" style="left:610px">
  <div class="who"><div class="pic" role="img" aria-label="Photo du client"></div><div><h4>Julien R. (Lille)</h4><small>CO-Founder</small><div class="stars">★★★★★</div></div></div>
  <p><q>“</q>Entrepreneur du bâtiment, j'ai commandé 20 polos et 20 vestes softshell personnalisés pour mon équipe. L'équipe graphique de Stampoli a adapté le logo au format nécessaire. Les vêtements sont impeccables pour travailler !</p>
  <div class="tail"></div>
</div>
<div class="abs dots"><i></i><i></i></div>

<section class="abs catalogue">
  <div class="abs section-title" style="left:491px;top:66px"><div class="bar" style="height:64px"></div><div><h2>Besoin d'idées ?</h2><p>Demander notre catalogue !</p></div></div>
  <p class="intro">Si vous êtes à la recherche d'idées originales, découvrez notre catalogue numérique ou papier comprenant une sélection d'objets publicitaires originaux et innovants. Vous pourrez également être informé des dernières nouveautés !</p>
  <a>Recevoir le catalogue</a>
</section>

<div class="abs accordion">
  <div class="acc-head">Votre spécialiste en Goodies originaux Ce qui caractérise des goodies originaux<span class="sign">−</span></div>
  <div class="acc-body">Les goodies sont également nommés cadeaux publicitaires ou cadeaux d'affaires. En effet, cette sélection d'objets regroupe différents articles nécessaires au développement d'une entreprise. Au-delà du simple parapluie, tour de cou ou textile publicitaire, les cadeaux publicitaires sont un support de communication intéressant. De nombreux objets tels que parapluie, stylos et mug sont concernés. Insérez facilement un texte, un logo ou une marque grâce à la gravure laser sur tout type d'objets. Les goodies publicitaires combinent à la fois utilité et support de communication à moindre coût. Découvrez des idées cadeaux classiques ou plus originaux parmi notre catalogue. Offrez à vos collaborateurs, clients et partenaires des cadeaux d'affaires qui permettront une croissance positive de votre image, utilisés au quotidien et laissant une empreinte visuelle durable lors de vos événements ou en remerciement.</div>
  <div class="acc-head">De nombreuses gammes de goodies simples ou origi-<span class="sign">+</span></div>
  <div class="acc-head">Qui est concerné par les goodies classiques ou originaux ?<span class="sign">+</span></div>
  <div class="acc-head">Les avantages des goodies<span class="sign">+</span></div>
  <div class="acc-head" style="border-bottom:0">Bénéficiez d'un accompagnement dès la conception<span class="sign">+</span></div>
</div>

<footer class="abs footer">
  <div class="abs brand" style="left:115px;top:52px">
    <div class="brand-square" style="width:26px;height:26px"></div>
    <div class="brand-name" style="color:#fff;font-size:22px">Stampoli</div>
  </div>
  <p class="abs about" style="left:115px;top:102px;width:195px">Stampoli est le fournisseur en ligne de référence pour vos objets publicitaires et cadeaux d'affaires personnalisés. Il s'adresse aux entreprises, associations, clubs sportifs, écoles et autres collectivités.</p>
  <div class="abs" style="left:324px;top:44px"><h5>Stampoli</h5><ul><li>- Qui sommes-nous ?</li><li>- Nos engagements</li><li>- Blog</li></ul></div>
  <div class="abs" style="left:488px;top:44px"><h5>Informations</h5><ul><li>- Conditions générales de vente</li><li>- Mentions légales</li><li>- Contact</li></ul></div>
  <div class="abs" style="left:719px;top:44px"><h5>Suivez-nous !</h5><ul class="social"><li><i></i>Fil Social</li><li><i></i>Micro Posts</li><li><i></i>Réseau Pro</li></ul></div>
  <div class="abs" style="left:857px;top:44px;width:230px"><h5>Inscrivez-vous à notre newsletter</h5><p class="about">Recevez en avant première les nouveautés et ventes exclusives sur nos objets publicitaires et goodies.</p><div class="newsletter"><span>Votre email</span><b>Subscribe</b></div></div>
  <div class="pay"><span>Payvio</span><span>Cardora</span><span>Vestra</span></div>
</footer>

</body>
</html>
```